IT Consulting Site Revamping for Marlune

I've put a skeleton together on my website, but realize I need some help (it's http://pilot.marlune-example.ca).
I've pulled together tidbits from other websites, but really need my site to be cleaned up, and really spruced up.
I primarily focus on the IT needs of small to medium size businesses, taking care of everything from their servers and networks down to their workstations.
I also want a page listing the vendors (and logos) that I work with including Quillsoft, Zentrix, Halvor, Brax, TL, RZO, VELK, Trevo, Gatemoor.
There should also be a simple form to get a quote that will email me.
The final design should communicate strength and reliability.
I would like this to be a fully functional website, that I can upload to Plumly Pages, with the same sort of pages that are existing on http://pilot.marlune-example.ca
Updates
Hey everyone,
Hi everyone,
Reason: Hi all,
There are some designers that would like to submit some new designs, so I'm extending the deadline.
Thanks,
Target Market(s)
Small to medium size business owners. This will primarily be males who work in the oil and gas industry.
Industry/Entity Type
Consulting
Look and feel
Each slider illustrates characteristics of the customer's brand and the style your logo design should communicate.

```html
<!DOCTYPE html>
<html lang="en">
<head>
<meta charset="utf-8">
<title>Marlune Solutions</title>
<link href="https://fonts.googleapis.com/css2?family=Arimo:wght@400;700&family=Marcellus&family=Marcellus+SC&family=PT+Sans:wght@400;700&family=Open+Sans:wght@600&display=swap" rel="stylesheet">
<style>
:root{
  --navy:#0c2f66;
  --nav-top:#1d4fa0;
  --nav-bottom:#0a2f6e;
  --body-blue:#1554a8;
  --panel:#f3f4f6;
  --footer:#062a55;
  --footer-line:#1a4172;
  --footer-text:#c9d3e0;
  --white:#ffffff;
}
*{box-sizing:border-box;margin:0;padding:0}
html,body{width:1016px;height:1200px;overflow:hidden;background:#fff}
body{position:relative;font-family:"Arimo",Arial,sans-serif}
.page-bg{position:absolute;left:0;top:0;width:706px;height:932px;background:#fcf9fa}

/* header */
.brand{position:absolute;left:38px;top:22px;display:flex;align-items:center;gap:10px}
.brand-dot{width:58px;height:58px;border-radius:50%;background:var(--body-blue)}
.brand-name{font:700 40px/1 "Arimo",sans-serif;color:var(--body-blue)}
.quick-links{position:absolute;right:48px;top:34px;display:flex;gap:14px}
.quick-link{display:flex;flex-direction:column;align-items:center;font-size:10px;color:#111}
.quick-link svg{height:20px;margin-bottom:3px}

/* nav */
.main-nav{position:absolute;left:36px;top:100px;width:933px;height:45px;background:linear-gradient(var(--nav-top),var(--nav-bottom));display:flex;align-items:center}
.nav-item{color:var(--white);font-size:18px;padding:0 27px;height:45px;line-height:45px;border-right:1px solid #2a5aa8}
.nav-item:last-of-type{border-right:0}
.search{position:absolute;right:18px;top:8px;width:194px;height:28px;border:1px solid #3a6ab6;border-radius:4px;background:#0d3577;color:#7aa0d8;font-size:12px;line-height:26px;padding-left:9px}
.search svg{position:absolute;right:8px;top:6px}

/* hero */
.hero{position:absolute;left:36px;top:145px;width:933px;height:329px;background:linear-gradient(90deg,#fff 0%,#f6f7f9 45%,#e9edf1 100%);overflow:hidden}
.hero-photo{position:absolute;right:0;top:0;width:440px;height:329px;background:radial-gradient(ellipse at 60% 45%,#e8d6cc 0%,#dcdfe4 40%,rgba(240,242,245,0) 75%)}
.hero-title{position:absolute;left:37px;top:86px;width:478px;font-family:"Marcellus",serif;color:var(--navy);text-shadow:2px 3px 4px rgba(0,0,0,.35);text-align:center}
.hero-title .line1{font-size:38px;white-space:nowrap}
.hero-title .line2{font-size:54px;margin-top:0}

/* vendors */
.vendor-strip{position:absolute;left:36px;top:474px;width:933px;height:63px;background:linear-gradient(#1c4d9e,#0a2e6d);display:flex;align-items:center}
.vendor-strip .arrow{width:34px;display:flex;justify-content:center}
.vendors{flex:1;display:flex;height:63px}
.vendor{flex:1;display:flex;align-items:center;justify-content:center;color:var(--white);font-size:21px;font-weight:700;border-right:1px solid #2b5aa5}
.vendor:last-child{border-right:0}

/* content */
.content{position:absolute;left:36px;top:537px;width:933px;height:395px;background:var(--panel)}
.products{position:absolute;left:19px;top:15px;width:190px}
.products-title{height:40px;background:linear-gradient(#1f56ab,#0b3174);border-radius:4px 4px 0 0;color:var(--white);font:22px/40px "Marcellus SC",serif;text-align:center;box-shadow:0 2px 3px rgba(0,0,0,.3)}
.products-list{margin-top:2px;height:322px;background:linear-gradient(90deg,#0a2d68,#1a4c98 50%,#0a2d68);border-radius:0 0 4px 4px;padding:4px 19px 0 16px;list-style:none}
.products-list li{color:#e6edf7;font-size:13px;height:34px;line-height:34px;padding-left:14px;border-bottom:1px solid #26559c}
.products-list li:last-child{border-bottom:0}
.welcome{position:absolute;left:236px;top:20px;width:670px}
.welcome h1{font:400 24px/1 "Marcellus SC",serif;color:var(--navy);margin-bottom:12px;letter-spacing:.3px;text-shadow:0 0 .5px var(--navy)}
.welcome p{color:var(--body-blue);font-size:13.6px;line-height:24px;text-align:justify;padding-left:4px;margin-bottom:24px;letter-spacing:-.1px}
.read-more{position:absolute;right:37px;bottom:12px;font-size:13px;color:#111}

/* footer */
.site-footer{position:absolute;left:0;top:932px;width:1000px;height:268px;background:var(--footer)}
.footer-col{position:absolute;top:28px}
.footer-col h2{font-size:15px;line-height:18px;color:var(--white);font-weight:700;margin-bottom:11px}
.footer-col ul{list-style:none;padding-left:6px}
.footer-col li{font:12px/36px "PT Sans",sans-serif;color:var(--footer-text)}
.col-info{left:59px}.col-service{left:243px}.col-service ul{padding-left:21px}.col-account{left:450px}.col-account ul{padding-left:11px}
.connect{position:absolute;left:568px;top:93px;width:199px;height:43px;border-radius:6px;background:linear-gradient(#2a63c0,#0b3477);color:var(--white);font:600 32px/43px "Open Sans",sans-serif;text-align:center}
.support-photo{position:absolute;left:786px;top:32px;width:164px;height:157px;border:3px solid #3a3f46;background:linear-gradient(135deg,#f4e8e0,#d9c6b8 55%,#eef0f2)}
.footer-rule{position:absolute;left:36px;top:208px;width:933px;border-top:1px solid var(--footer-line)}
.copyright{position:absolute;left:45px;top:222px;font:11px "PT Sans",sans-serif;color:#8f9db0}
.follow{position:absolute;left:745px;top:218px;display:flex;align-items:center;gap:10px;color:var(--white);font:700 14px "PT Sans",sans-serif}
.social{font:700 12px "PT Sans",sans-serif;color:var(--white)}
</style>
</head>
<body>
<div class="page-bg"></div>

<header>
  <div class="brand"><span class="brand-dot"></span><span class="brand-name">Marlune</span></div>
  <nav class="quick-links">
    <div class="quick-link"><svg viewBox="0 0 20 20" width="20"><path d="M10 2 1 10h3v8h4v-5h4v5h4v-8h3z" fill="#0c2f66"/></svg>Home</div>
    <div class="quick-link"><svg viewBox="0 0 20 20" width="20"><circle cx="10" cy="10" r="6" fill="none" stroke="#0c2f66" stroke-width="4" stroke-dasharray="3 2"/><circle cx="10" cy="10" r="3.5" fill="none" stroke="#0c2f66" stroke-width="2"/></svg>Services</div>
    <div class="quick-link"><svg viewBox="0 0 22 20" width="22"><rect x="1" y="5" width="20" height="13" fill="#0c2f66"/><path d="M1 5l10 7 10-7" fill="none" stroke="#fff" stroke-width="1.5"/></svg>Contact us</div>
  </nav>
</header>

<nav class="main-nav">
  <span class="nav-item">Home</span>
  <span class="nav-item">Our Services</span>
  <span class="nav-item">About Us</span>
  <span class="nav-item">Our Products</span>
  <span class="nav-item">Contact Us</span>
  <div class="search">Search<svg width="14" height="14" viewBox="0 0 14 14"><circle cx="8" cy="6" r="4" fill="none" stroke="#fff" stroke-width="1.6"/><path d="M5 9 1 13" stroke="#fff" stroke-width="1.8"/></svg></div>
</nav>

<section class="hero">
  <div class="hero-photo" role="img" aria-label="Photo of a smiling support consultant in a bright office"></div>
  <div class="hero-title"><div class="line1">Easy, Affordable &amp; Reliable</div><div class="line2">Services</div></div>
</section>

<section class="vendor-strip">
  <div class="arrow"><svg width="14" height="40"><path d="M12 2 3 20l9 18" fill="none" stroke="#fff" stroke-width="2"/></svg></div>
  <div class="vendors">
    <span class="vendor">Quillsoft</span><span class="vendor">TL</span><span class="vendor">RZO</span><span class="vendor">Brax</span><span class="vendor">Zentrix</span><span class="vendor">Trevo</span><span class="vendor">Gatemoor</span>
  </div>
  <div class="arrow"><svg width="14" height="40"><path d="M2 2l9 18-9 18" fill="none" stroke="#fff" stroke-width="2"/></svg></div>
</section>

<main class="content">
  <aside class="products">
    <div class="products-title">Our Products</div>
    <ul class="products-list">
      <li>Accessories</li><li>Computer Cases</li><li>Controller / RAID Cards</li><li>Processors</li><li>DVD Burners</li><li>Fans (cooling)</li><li>Flash Drivers &amp; Memory</li><li>Hard Disk &amp; SSD</li><li>Bags &amp; Sleeves</li>
    </ul>
  </aside>
  <article class="welcome">
    <h1>Welcome To Our Website</h1>
    <p>Marlune Solutions is a computer solutions provider and IT consulting firm that supports a wide variety of local small businesses in the Calgary area primarily. Our company also provides IT services to businesses throughout Alberta on special projects.</p>
    <p>Marlune has been trusted for over the last 7 years by small business companies like yours. Whether you are looking for an ongoing computer support company, looking to outsource your small business computer work, or just looking for a computer company to help you solve a computer problem, Marlune is your right choice.</p>
    <p>We have a diversity of small business support solutions. We provide in office, over the phone, remote or drop-off computer technical support services to small business.</p>
    <p>Our computer technicians and network professionals understand that your business operations hinge on computer and network availability.</p>
  </article>
  <span class="read-more">&gt;&gt; Read More...</span>
</main>

<footer class="site-footer">
  <div class="footer-col col-info"><h2>Information</h2><ul><li>About</li><li>Delivery</li><li>Privacy Policy</li><li>Terms &amp; Conditions</li></ul></div>
  <div class="footer-col col-service"><h2>Customer Service</h2><ul><li>Brand</li><li>Contacts</li><li>Returns</li><li>Site Map</li></ul></div>
  <div class="footer-col col-account"><h2>My Account</h2><ul><li>My Account</li><li>Order History</li><li>Wish List</li><li>Newsletter</li></ul></div>
  <div class="connect">Connect Us</div>
  <div class="support-photo" role="img" aria-label="Photo of a support agent with headset, 24 hour call now badge"></div>
  <div class="footer-rule"></div>
  <div class="copyright">Copyright 2012.All Rights Reserved.</div>
  <div class="follow">Follow Us :<span class="social">Linkora</span><span class="social">Buzzlet</span><span class="social">Newsrill</span></div>
</footer>
</body>
</html>
```